Vantrel Card

We want a business card that shows people who we are the log attached was designed by the designers on craft hive,we are using the OO in the logo (speech bubbles as our icon,so please make that part of the card ) keep the colouring the same as the logo design and we will be using high end production on the card using silver foil as the icon to make it stand out.
As Vantrel we specialise in finding influencers through social networks for brands, so if you used flimbo to comment about sports products and you were followed by of lot of users and interacted with those users then the algorithm finds you and we contact you to work for our clients as a company we then have a set of influencers that we use to support new sports products.
Also we use our algorithm to help athletes,models etc to be scored via there digital influence so when say Vorta KX ask me to find a skater that is not so much a podium rider but is more digital focused for a digital campaign then we work out who those guys or girls are to help Vorta KX
Vantrel is the name of the product and company, However I just wanted to give you the rationale of why we chose vantrel in the first place. Marbo itself is an 'abbreviation' from the proper name Alsander Wick from Tale of the Iron Hills. The character was able to look into the eskavor (sometimes translated as "Seeing Stone" but literally meaning "Farsighted" or "One that Sees from Afar") and see into the far corners of the Universe. Much in the same way as the platform has been developed is able to look into the far corners of the social network arena to help brands and Athletes will be able to see how they rated....but don't worry i don't go running around in the woods with a foam Axe and an army of dwarfs!!!
Digital Directors,Brand Directors,Athletes,Models,Celebrities and agents
Business

```html
<!DOCTYPE html>
<html lang="en">
<head>
<meta charset="utf-8">
<title>Vantrel Business Card</title>
<link rel="stylesheet" href="https://fonts.googleapis.com/css2?family=Poppins:wght@300;400;600&display=swap">
<style>
  :root {
    --bg: #ececed;
    --card-dark: #2f2f32;
    --card-light: #f6f6f5;
    --brand-blue: #3aa8df;
    --ink: #5a5a5e;
    --ink-strong: #4a4a4e;
  }
  * { box-sizing: border-box; margin: 0; padding: 0; }
  html, body {
    width: 1200px; height: 1000px; overflow: hidden;
    background: var(--bg);
    font-family: "Poppins", sans-serif;
  }
  .canvas { position: relative; width: 1200px; height: 1000px; }
  .card { position: absolute; left: 250px; width: 700px; height: 425px; }
  .card--front { top: 40px; }
  .card--back { top: 520px; }
  .card-shape { position: absolute; inset: 0; width: 700px; height: 425px; }
  .card--front .card-shape { fill: var(--card-dark); }
  .card--back .card-shape { fill: var(--card-light); }

  .brand-name {
    position: absolute;
    font-weight: 600;
    color: var(--brand-blue);
    letter-spacing: 1px;
    line-height: 1;
  }
  .card--front .brand-name { left: 0; width: 700px; top: 150px; text-align: center; font-size: 96px; }
  .card--back .brand-name { left: 52px; top: 150px; font-size: 58px; }

  .website {
    position: absolute; left: 58px; top: 258px;
    font-size: 17px; font-weight: 300; color: var(--brand-blue);
  }

  .contact {
    position: absolute; left: 392px; top: 92px; width: 270px;
    font-size: 15.5px; font-weight: 300; color: var(--ink); line-height: 1.3;
  }
  .contact-name { font-size: 20px; font-weight: 600; color: var(--ink-strong); }
  .contact-row { display: flex; gap: 8px; }
  .contact-label { width: 10px; font-weight: 600; color: var(--brand-blue); }
  .contact-rule { height: 2px; background: var(--brand-blue); margin: 5px -20px 5px 0; }
</style>
</head>
<body>
<main class="canvas">
  <section class="card card--front" aria-label="Card front">
    <svg class="card-shape" viewBox="0 0 560 340" aria-hidden="true">
      <circle cx="150" cy="150" r="140"/>
      <circle cx="400" cy="160" r="150"/>
      <polygon points="225,255 290,245 282,335"/>
      <polygon points="300,270 365,292 288,335"/>
    </svg>
    <div class="brand-name">vantrel</div>
  </section>

  <section class="card card--back" aria-label="Card back">
    <svg class="card-shape" viewBox="0 0 560 340" aria-hidden="true">
      <circle cx="150" cy="150" r="140"/>
      <circle cx="400" cy="160" r="150"/>
      <polygon points="225,255 290,245 282,335"/>
      <polygon points="300,270 365,292 288,335"/>
    </svg>
    <div class="brand-name">vantrel</div>
    <div class="website">www.vantrel.co.uk</div>
    <div class="contact">
      <div class="contact-name">Edwin Maraway</div>
      <div>cheif executive officer</div>
      <div class="contact-row"><span class="contact-label">e</span><span>hello@vantrel.co.uk</span></div>
      <div class="contact-row"><span class="contact-label">m</span><span>020 4410 2286</span></div>
      <div class="contact-rule"></div>
      <div>Vantrel Limited</div>
      <div>14 Larkspur Row,</div>
      <div>Ellingham Vale, Harbrook,</div>
      <div>HK12 7QD</div>
      <div class="contact-row"><span class="contact-label">t</span><span>020 3917 6640</span></div>
      <div class="contact-row"><span class="contact-label">f</span><span>020 3917 6641</span></div>
    </div>
  </section>
</main>
</body>
</html>
```